Cybersecurity Course - Bastion Trailplan: HOLV TPX Program

this is a graphic for a course I will launch. I have attached the ebook that will accompany the course. Logo also attached.

Size is 1280 x 720 pixels, with a minimum width of 640 pixels. The aspect ratio should be 16:9. The maximum file size is 2 MB.

Title: Bastion Trailplan: HOLV TPX Program
- MASTER Governance Risk Management & Compliance (GRC) with HOLV TPX 2.0
- Learn through real-world industry applications, examples, and samples
- Access downloadable HOLV TPX 2.0 resources and experience a guided walkthrough with a mentor

Target Market(s)

IT services

Industry/Entity Type

cybersecurity

Colors
0054AA
0677BA
7BADD7
CADEEF
E8F1F8

Requirements
Must have
• 1280 x 720 pixel

```html
<!DOCTYPE html>
<html lang="en">
<head>
<meta charset="UTF-8">
<title>Bastion Trailplan: HOLV TPX Program</title>
<link rel="stylesheet" href="https://fonts.googleapis.com/css2?family=Bebas+Neue&family=Barlow+Condensed:wght@700&family=Roboto+Condensed:wght@400&display=swap">
<style>
  :root {
    --page: #1c1c1c;
    --ink: #1d1d1f;
    --navy: #0054aa;
    --mid-blue: #0677ba;
    --sky: #7badd7;
    --pale: #cadeef;
    --mist: #e8f1f8;
    --gold-dark: #b8934a;
    --gold-light: #f4e9a0;
    --white: #ffffff;
  }
  * { margin: 0; padding: 0; box-sizing: border-box; }
  html, body { width: 1200px; height: 1000px; overflow: hidden; background: var(--page); }
  .banner {
    position: absolute; left: 0; top: 162px; width: 1200px; height: 675px; overflow: hidden;
    background: linear-gradient(180deg, var(--white) 0%, var(--mist) 14%, var(--pale) 32%, #8cc6ee 55%, #5a9ad6 78%, #2a68b8 92%, var(--navy) 100%);
  }
  .brand {
    position: absolute; left: 353px; top: 92px; transform: translate(-50%, -50%);
    display: flex; align-items: center; gap: 10px;
    font-family: 'Roboto Condensed', sans-serif; font-size: 22px; color: var(--mid-blue); white-space: nowrap;
  }
  .brand-dot { width: 16px; height: 16px; border-radius: 50%; background: var(--mid-blue); }
  .title {
    position: absolute; left: 49px; top: 170px; width: 641px;
    font-family: 'Bebas Neue', sans-serif; font-weight: 400; font-size: 106px; line-height: 1; color: var(--ink);
    white-space: nowrap; transform: scaleY(1.42); transform-origin: left top;
  }
  .program-band {
    position: absolute; left: 50px; top: 308px; width: 640px; height: 61px;
    background: linear-gradient(90deg, var(--gold-dark) 0%, #d9c27a 30%, var(--gold-light) 55%, #d4b870 80%, var(--gold-dark) 100%);
    display: flex; align-items: center; justify-content: center;
    font-family: 'Barlow Condensed', sans-serif; font-weight: 700; font-size: 52px; color: var(--navy); letter-spacing: 0.5px;
  }
  .benefits {
    position: absolute; left: 50px; top: 390px; width: 640px; list-style: none;
    font-family: 'Roboto Condensed', sans-serif; font-size: 26px; line-height: 35px; color: var(--white);
  }
  .benefits li { position: relative; padding-left: 21px; width: 640px; }
  .benefits li::before {
    content: ""; position: absolute; left: 5px; top: 14px;
    border-left: 7px solid var(--white); border-top: 4px solid transparent; border-bottom: 4px solid transparent;
  }
  .emblem { position: absolute; left: 0; top: 0; }
</style>
</head>
<body>
  <section class="banner">
    <div class="brand"><span class="brand-dot"></span>Ridgeward Academy</div>
    <h1 class="title">BASTION TRAILPLAN</h1>
    <div class="program-band">HOLV TPX PROGRAM</div>
    <ul class="benefits">
      <li>MASTER Governance Risk Management &amp; Compliance (GRC) with HOLV TPX 2.0</li>
      <li>Learn through real-world industry applications, examples, and samples</li>
      <li>Access downloadable HOLV TPX 2.0 resources and experience a guided walkthrough with a mentor</li>
    </ul>
    <svg class="emblem" width="1200" height="675" viewBox="0 0 1200 675">
      <defs>
        <radialGradient id="landscape" cx="0.55" cy="0.5" r="0.7">
          <stop offset="0" stop-color="#4f7f34"/>
          <stop offset="0.45" stop-color="#3d6a28"/>
          <stop offset="0.8" stop-color="#6c8f4c"/>
          <stop offset="1" stop-color="#8fa571"/>
        </radialGradient>
        <linearGradient id="gold" x1="0" y1="0" x2="1" y2="1">
          <stop offset="0" stop-color="#c9a85e"/>
          <stop offset="0.5" stop-color="#f1e2a0"/>
          <stop offset="1" stop-color="#b8934a"/>
        </linearGradient>
      </defs>
      <path class="shield" role="img" aria-label="Miniature green landscape with a winding road, cars, map pins and a keyhole inside a shield"
        d="M1054 61 Q970 148 814 162 Q808 420 1054 614 Q1150 570 1200 533 L1200 146 Q1110 130 1054 61 Z"
        fill="url(#landscape)" stroke="url(#gold)" stroke-width="5"/>
    </svg>
  </section>
</body>
</html>
```